Modern and sophisticated web design for architect/designer

Lumo Vant is a Building Design & Drafting studio based in Nedlands Western Australia, providing a high quality and complete client service from concept design through Council planning approvals and building licenses to construction drawings for kitchens and bathrooms, extensions, additions, renovations and new homes.

Lumo Vant is looking for a new qwerty design that *is different from a normal* 2/3 column website. The website design must be very arty, clean and catchy. This design needs to be very different and must not look like a downloadable template.

The design must be able to display a lot of photos for the different projects.

The design must comply with W3C standards (i.e. use of fonts) and must be delivered to us in A PSD layered format.

Here are a couple of example website designs that exemplify what I am after:
1) http://www.prtd.com.au/
2) http://www.martinholsbyarchitect.com/en/
3) http://veromiks.com/

I particularly like numbers 1 and 2. The third, Veromiks, jumps around a little between pages as it is actually several companies. I prefer the page design to remain steady if possible.

I like the very clever nature of number 1 (PRTD). It captures the interest, although slightly gimmicky, however I think it doesn't overpower. Its modern, and visual.

I like the clean elegant design of number 2 (Holsby), it simply delivers everything necessary in a clear intelligent manner, its attractive, menu is clever simple to use and attractive.

I would be very happy to have either of these websites.

here is another one:
4) http://www.tqarchitect.com.au/

Although this is similarly elegant, it appears quite dated. I don't like the thumbnails that you click on in the gallery, its quite clumsy. It looks minimalist, and IS minimalist, doesn't look like there is much option to expand other than changing the pictures.

If you look at my own website:
http://www.lumovant.com.au

I designed and built it myself without any skills or experience. I had to use a generic photo album generator which was worse than useless, the point I am trying to make is I tried to make the menu system a little unusual, I tried to keep the pages neat and tidy, and totally used the "black website" method. However I am more inclined to go with the lighter/white pages of (1) and (2) above because they tend to show photos better.

Dear Designers. 

ArtHive Administration has worked to provide a more comprehensive brief. Please review the amended description. 

Kind Regards, Wesley. 

Target Market(s)

Target market is people who are looking to renovate their home

Industry/Entity Type

Construction

Requirements
Must have
• The brief is to design a visual modern, elegant, sophisticated website for a small scale designer/photographer/architect that looks itself like it is designed. Not off the shelf, simple and dated. Basically the design itself has to exemplify me, it has to say "this guy is a designer, and he is good at it".

```html
<!DOCTYPE html>
<html lang="en">
<head>
<meta charset="utf-8">
<title>Lumo Vant Design – Building Design &amp; Drafting Studio</title>
<link rel="stylesheet" href="https://fonts.googleapis.com/css2?family=Orbitron:wght@400;500&family=Open+Sans:wght@400;600&family=Rajdhani:wght@500;600&display=swap">
<style>
:root{
  --red:#d7262d;
  --navy:#0c3f78;
  --blue:#0e5aa8;
  --violet:#3a34a2;
  --ink:#333;
  --header:#eeeeee;
  --tab:#f4f4f4;
  --dark:#111;
  --side:#3a3a3a;
  --white:#fff;
}
*{box-sizing:border-box;margin:0;padding:0}
html,body{width:1112px;height:1200px;overflow:hidden;background:var(--white)}
.stage{position:relative;width:1210px;height:1309px;transform:scale(.919,.9167);transform-origin:0 0;font-family:"Open Sans",sans-serif;color:var(--ink)}
.backdrop{position:absolute;inset:0}
.page{position:absolute;left:103px;top:0;width:1000px;height:1309px;background:var(--white);box-shadow:0 0 8px rgba(0,0,0,.25)}
.abs{position:absolute}

/* header */
.header{left:0;top:0;width:1000px;height:131px;background:var(--header)}
.brand{left:19px;top:50px;display:flex;align-items:center;gap:10px;font-family:"Orbitron",sans-serif;font-weight:500;font-size:19px;letter-spacing:3px;color:#2b2b2b}
.brand-mark{width:14px;height:14px;background:#2b2b2b}
.phone{right:262px;top:16px;font-size:24px;color:#444}
.social{right:11px;top:11px;display:flex;gap:0}
.social span{display:block;width:39px;height:43px;background:#5e5e5e;border-bottom:4px solid}
.nav{left:285px;top:72px;display:flex}
.nav a{display:block;width:143px;height:60px;line-height:62px;text-align:center;background:var(--tab);border:1px solid #ddd;font-family:"Orbitron",sans-serif;font-size:18px;color:#444;text-decoration:none}
.navbar{left:0;top:131px;width:1000px;height:14px;display:flex}
.navbar i{display:block;height:14px}

/* hero */
.hero{left:0;top:145px;width:1000px;height:408px;overflow:hidden}
.hero-photo{position:absolute;inset:0;background:linear-gradient(135deg,#5c4a44 0%,#7a5040 35%,#3d2a22 70%,#1e1410 100%)}
.hero-shade{position:absolute;inset:0}
.hero-title{position:absolute;right:22px;top:80px;text-align:right;font-family:"Orbitron",sans-serif;font-weight:500;color:var(--white);font-size:27px;line-height:45px}
.hero-title em{font-style:normal;color:var(--red)}
.hero-quote{position:absolute;right:23px;top:183px;width:470px;text-align:right;color:var(--white);font-size:17px;line-height:26px;letter-spacing:.3px}
.dots{position:absolute;left:697px;top:364px;display:flex;align-items:center;gap:8px}
.dots b{display:block;width:15px;height:15px;background:#bbb}
.dots b.on{background:var(--red)}

/* projects */
.tile{position:absolute;width:250px;height:250px}
.tile-photo{background:linear-gradient(160deg,#6f6a55,#3a3426 60%,#1d1a14)}
.tile-label{display:flex;flex-direction:column;align-items:center;justify-content:center;color:var(--white);text-align:center}
.tile-label h2{font-family:"Rajdhani",sans-serif;font-weight:600;font-size:40px;line-height:40px;letter-spacing:1px}
.tile-label p{font-size:18px;margin-top:6px}
.red{background:var(--red)}
.violet{background:var(--violet)}
.thumb{position:absolute;width:126px;height:124px}
.summary{padding:22px 27px}
.summary h2{font-family:"Rajdhani",sans-serif;font-weight:600;font-size:40px;color:#222;line-height:44px}
.summary p{font-size:13px;line-height:20px;color:#222;margin-top:10px}
.btn{position:absolute;left:27px;top:196px;width:202px;height:36px;background:var(--red);color:var(--white);font-family:"Rajdhani",sans-serif;font-size:19px;font-weight:500;line-height:36px;padding-left:13px;text-decoration:none}
.btn svg{position:absolute;right:4px;top:4px}

/* footer */
.footer{left:0;top:1062px;width:1000px;height:208px;background:var(--dark);color:var(--white)}
.footer-rule{position:absolute;left:0;top:38px;width:1000px;height:5px;background:var(--red)}
.col{position:absolute;top:0}
.col h3{font-family:"Rajdhani",sans-serif;font-weight:500;font-size:21px;line-height:40px}
.col ul{list-style:none;font-size:12px;line-height:22px;margin-top:15px;padding-left:5px}
.col p{font-size:12px;line-height:18px}
.phone-form{position:absolute;left:0;top:137px;display:flex}
.phone-form span{display:block;width:176px;height:37px;background:var(--white);color:#555;font-style:italic;font-size:12px;line-height:37px;padding-left:18px}
.phone-form b{display:block;width:38px;height:37px;background:var(--blue);position:relative}
.mini{display:flex;gap:5px;margin-top:18px}
.mini span{display:block;width:23px;height:23px}
.copyright{left:0;top:1270px;width:1000px;height:39px;background:#1c1c1c;color:#ddd;font-size:10px;text-align:center;line-height:42px}
</style>
</head>
<body>
<div class="stage">
  <svg class="backdrop" width="1210" height="1309" aria-hidden="true">
    <rect x="0" y="0" width="96" height="1309" fill="var(--side)"/>
    <polygon points="0,1309 0,1292 96,1178 96,1309" fill="#fff"/>
    <polygon points="1110,0 1210,0 1210,2 1110,107" fill="var(--side)"/>
  </svg>

  <div class="page">
    <header class="header abs">
      <div class="brand abs"><span class="brand-mark"></span>LUMO VANT DESIGN</div>
      <div class="phone abs">+44(0) 20946 13570</div>
      <div class="social abs" aria-label="Social links">
        <span style="border-color:#1b62b2"></span>
        <span style="border-color:var(--red)"></span>
        <span style="border-color:#0d63a8"></span>
        <span style="border-color:#e67e22"></span>
        <span style="border-color:var(--red)"></span>
        <span style="border-color:#2aa3e0"></span>
      </div>
      <nav class="nav abs">
        <a href="#">Home</a><a href="#">About us</a><a href="#">Services</a><a href="#">Projects</a><a href="#">Contact</a>
      </nav>
    </header>
    <div class="navbar abs">
      <i style="width:285px;background:#333"></i>
      <i style="width:144px;background:var(--red)"></i>
      <i style="width:141px;background:var(--navy)"></i>
      <i style="width:430px;background:var(--blue)"></i>
    </div>
    <svg class="abs" style="left:345px;top:116px" width="28" height="16" aria-hidden="true"><polygon points="0,16 14,1 28,16" fill="var(--red)"/></svg>

    <section class="hero abs">
      <div class="hero-photo" role="img" aria-label="Photo of a modern kitchen with dark timber cabinets and a red stone splashback"></div>
      <svg class="hero-shade" width="1000" height="408" aria-hidden="true"><polygon points="712,0 1000,0 1000,408 497,408" fill="#000"/></svg>
      <h1 class="hero-title">BUILDING <em>DESIGN</em><br>&amp; DRAFTING STUDIO</h1>
      <p class="hero-quote">“Providing a high quality and complete client service from concept design through Council planning approvals and building licenses to construction drawings for kitchens and bathrooms, extensions, additions, renovations and new homes.”</p>
      <div class="dots">
        <svg width="8" height="12" aria-hidden="true"><polygon points="7,0 0,6 7,12" fill="#fff"/></svg>
        <span style="width:16px"></span>
        <b></b><b class="on"></b><b></b><b></b>
        <span style="width:12px"></span>
        <svg width="8" height="12" aria-hidden="true"><polygon points="1,0 8,6 1,12" fill="#fff"/></svg>
      </div>
    </section>

    <section class="abs" style="left:0;top:553px;width:1000px;height:499px">
      <div class="tile tile-photo" style="left:0;top:0;height:240px;background:linear-gradient(160deg,#9aa07a,#4b3a2b 55%,#2a2019)" role="img" aria-label="Photo of a timber deck and garden pavilion at dusk"></div>
      <div class="abs red" style="left:0;top:240px;width:250px;height:10px"></div>
      <div class="tile tile-label red" style="left:250px;top:0"><h2>PROJECTS</h2><p>Project Name</p></div>
      <div class="tile tile-photo" style="left:500px;top:0;height:240px;background:linear-gradient(170deg,#4f6f95,#3d4a3a 45%,#6a4a25 70%,#1c1a12)" role="img" aria-label="Photo of a brick cottage lit at night behind a garden"></div>
      <div class="abs violet" style="left:500px;top:240px;width:250px;height:10px"></div>
      <div class="tile tile-label violet" style="left:750px;top:0"><h2>PROJECTS</h2><p>Project Name</p></div>

      <div class="tile tile-photo" style="left:0;top:250px;background:linear-gradient(180deg,#3f78c6,#7ea4d8 40%,#9a7a5a 75%,#4e5a3a)" role="img" aria-label="Photo of a two-storey modern home with timber-framed windows"></div>
      <div class="tile tile-label violet" style="left:250px;top:250px"><h2>PROJECTS</h2><p>Project Name</p></div>
      <div class="thumb" style="left:500px;top:250px;background:linear-gradient(150deg,#7a8aa6,#1e2333)" role="img" aria-label="Photo of a curved glass stair interior"></div>
      <div class="thumb" style="left:626px;top:250px;background:linear-gradient(160deg,#9aa07a,#4b3a2b)" role="img" aria-label="Photo of a timber deck project"></div>
      <div class="thumb" style="left:500px;top:374px;background:linear-gradient(180deg,#5f8fd0,#9a7a5a)" role="img" aria-label="Photo of a modern two-storey home"></div>
      <div class="thumb" style="left:626px;top:374px;background:linear-gradient(170deg,#3d4a3a,#7a5428 60%,#1c1a12)" role="img" aria-label="Photo of a brick cottage at night"></div>
      <div class="abs summary" style="left:752px;top:250px;width:248px;height:249px;background:#f7f7f7">
        <h2>PROJECTS</h2>
        <p>Lorem ipsum dolor sit amet, consectetur adipiscing elit. Duis laoreet pulvinar est, at vestibulum nibh varius ac. Phasellus placerat ante metus, a porttitor.</p>
        <a class="btn" href="#">View all projects
          <svg width="28" height="28" aria-hidden="true"><rect width="28" height="28" fill="#fff"/><path d="M6 14h13M13 8l6 6-6 6" stroke="var(--red)" stroke-width="3" fill="none"/></svg>
        </a>
      </div>
    </section>

    <footer class="footer abs">
      <div class="footer-rule"></div>
      <div class="col" style="left:19px">
        <h3>Quick Links</h3>
        <ul><li>Council planning approvals</li><li>Construction drawings</li><li>Extensions</li><li>Building licenses</li><li>Renovations and new homes</li></ul>
      </div>
      <div class="col" style="left:261px">
        <h3>Quick Links</h3>
        <ul style="margin-top:10px"><li>Contact us</li><li>Site map</li><li>Cookie policy</li></ul>
      </div>
      <div class="col" style="left:511px;width:220px">
        <h3>Start Designing</h3>
        <p style="margin-top:7px;line-height:20px">Do you have a project that need designing? Fill out your phone number below and we will call you.<br>Start your project today</p>
        <div class="phone-form"><span>Phone number</span><b><svg width="38" height="37" aria-hidden="true"><circle cx="19" cy="18.5" r="8" stroke="#fff" stroke-width="1.5" fill="none"/><path d="M14.5 18.5h8M19.5 15l3.5 3.5-3.5 3.5" stroke="#fff" stroke-width="1.5" fill="none"/></svg></b></div>
      </div>
      <div class="col" style="left:760px">
        <h3>Keep in Touch</h3>
        <p style="margin-top:12px">18 Harlow Lane,<br>State, Country<br>Zipcode<br>tel: +44(0) 20946 1357<br>info@lumovantdesign.com</p>
        <div class="mini"><span style="background:#3b5a9a"></span><span style="background:#0e6fb0"></span><span style="background:#2aa3e0"></span></div>
      </div>
    </footer>
    <div class="copyright abs">Copyright © 2013 Lumo Vant. Use of this website constitutes acceptance of our User Agreement and Privacy Policy.</div>
  </div>
</div>
</body>
</html>
```